"BrindleApps" Website Design

We are a new web/social media development company called "BrindleApps". We need a website homepage and 1 inner page designed. We want visitors to our site to know in the first few seconds that we design and build "apps". We do not want people leaving our homepage not having at least the high level understanding that we design and build "Apps".
We currently have a landing page up at www. brindleapps .example
We specialise in building bespoke
- Torvix apps
- Lumet apps
- Plimnet Apps
- Quorvel Apps
- Wendolite Apps
- Web applications
- Vub Apps
- Social Media Marketing Solutions & Strategies
We need a website design concept that is clean, crisp, fresh and says the following about us...
We are a modern web 2.0 company (simple but striking/bold)
We are friendly, professional but dynamic and NOT boring
We are experts in developing apps
We are innovative, modern, energetic and funky
We deliver quality
We can develop to all budgets
The services we offer...
1. App Consultative Services
strategy and planning services for businesses who know they should have an "App" but dont know where to start or what type of App would achieve the best ROI in relation to their objectives.
2. Persona Driven Development leading to Solution & Requirement Design
We help the client understand their audience/target market by developing typical personas of the people who they want to use the app, these personas then drive the solution and the technical requirements. During this process we also pull together written technical specs that outlines the functionality of the app including any mandatory corporate requirements, plus screen-by-screen wireframes of their app with information about page transitions/navigation and any usability requiremens
3. App Design/User Experience Design
We develop a creative look and feel that delivers an outstanding user experience.
We develop Functional Design Specs showing the planned UI (User Interface) design, including the solution design and art direction following client sign off this is passed onto the development team to be programmed along with the apps features.
4. App Development
Turning the idea into a fully functional product with great UI and UX.
5. Maintenance
We offer a range of maintenance packages to suit all budgets, but give our clients piece of mind that there is always someone to call on when problems arise.
Our target audience is
1. anyone with an "App Idea" who needs to get from idea to production
and also
2. small and medium businesses and organisations.
PLEASE NOTE - We do not want a design churned out on an existing website template, so please dont waste your time if this is your normal design process, we will only consider bespoke design concepts that have really considered our brand and needs.
We expect to need additional pages designed which we will obviously look to offer the work to the designer who we choose in this competition.
Attached is a document containing links to websites with a mobile related theme that we like so you can get a feel for our likes and expectations, in addition we have attached our company logo for use in the design.
We dont have any photos or images to use, but are more than happy to pay for stockphotos etc. that are to be used in the final design.
We have not developed the text content or header titles yet so will need placeholder text/headers in place. Once we have the design we have the intention of working the content into the design and making it very search engine friendly, so we are happy for dummy text to be used in the design process unless you feel like making the text relevant.
Thanks for all the designs so far. General feedback relating to all designs...
Although nice, at present there isnt much "personality" in the designs and in most instances there is too much noise, could you please try and simplify the designs and reduce the amount of things for someone to look at but especially reduce the amount of text read.
3. Increase the amount of space
4. Be bolder with the use of the app brand logos
5. Maybe use more images of different well known smartphone handsets.
6. Vary the size of the typography more
7. Maybe try more vibrant colour combinations, especially with the text
Thanks and good luck
Hi there,
Just to add to the design concept ideas, ive had this image in my mind of the company logo somehow taking centre stage with all things "App" bursting out of it in a fun firework type of way (so smartphones, app brand logos, little square app icons etc.)
Not sure if this is a concept anyone want to attempt to pull something together on but trying to get away from the real "corporate" look. Apps are fun, exciting and interactive, i guess i want the website and the company to get that across about our company, but still get the message across that we are quality driven.
Thanks!
Target Market(s)
and also
Industry/Entity Type
Building
Requirements
Must have
- Clean
Crisp
Not too noisy, with space to breath and read without being overloaded by info.
4 or 5 persistant navigation links (e.g. About, Services, App Platforms, Contact Us, Blog)
The inner page needs to have a subtle contact form - this shouldnt be the focus of the page but just be a feature of it as we intend to have this as a feature on most of the inner pages. The contact form needs space to add info about project, and also a note stating that by submitting their idea we are automatically guaranteeing non disclosure.
Nice to have
- Other things the homepage and maybe the inner pages
A "Join our Plimnet Fanpage"
A "Follow us on Drosk" link
A space for our drosk/blog/news feed
Should not have
- Should not be based on an off the shelf template layout

```html
<!DOCTYPE html>
<html lang="en">
<head>
<meta charset="utf-8">
<title>BrindleApps – Home</title>
<link rel="stylesheet" href="https://fonts.googleapis.com/css2?family=Cabin:wght@400;500;600;700&family=Arimo:wght@400;700&display=swap">
<style>
  :root {
    --green: #3aae3a;
    --green-dark: #248a24;
    --text: #1c1c1c;
    --muted: #3a3a3a;
    --band-top: #8c8c8c;
    --band-bottom: #555;
    --footer: #0d0d0d;
    --footer-text: #f2f2f2;
    --heading: "Cabin", "Arimo", sans-serif;
    --body: "Arimo", Arial, sans-serif;
  }
  * { box-sizing: border-box; margin: 0; padding: 0; }
  html, body { width: 1200px; height: 1070px; overflow: hidden; }
  body { font-family: var(--body); color: var(--text); background: #fff; }
  .page {
    position: relative; width: 1200px; height: 1070px; overflow: hidden;
    background: linear-gradient(160deg, #f1f2f5 0%, #fff 38%, #fff 100%);
  }
  .page::before {
    content: ""; position: absolute; left: 380px; top: -80px; width: 900px; height: 380px;
    background: linear-gradient(200deg, rgba(220,224,232,.55), rgba(255,255,255,0));
    transform: skewX(-30deg);
  }
  .abs { position: absolute; }

  /* brand */
  .brand { left: 64px; top: 22px; width: 200px; }
  .brand-mark { width: 120px; height: 108px; border-radius: 50%; background: var(--green); }
  .brand-name { margin-top: 12px; font: 600 30px/1 var(--heading); color: #3b3b3b; letter-spacing: -.5px; }

  /* nav */
  .main-nav { left: 532px; top: 43px; display: flex; align-items: center; }
  .main-nav a { font: 700 17px/1 var(--body); color: #111; text-decoration: none; margin-right: 28px; }
  .main-nav a.is-current {
    background: linear-gradient(#5fd04f, #2d9a2d); color: #fff; border: 2px solid #1f7a1f;
    border-radius: 16px; padding: 7px 16px; margin-right: 12px;
  }

  /* hero */
  .hero-photo {
    left: 250px; top: 90px; width: 610px; height: 484px;
    background:
      radial-gradient(ellipse 120px 150px at 62% 38%, rgba(224,186,160,.85), rgba(224,186,160,0) 100%),
      radial-gradient(ellipse 110px 140px at 84% 36%, rgba(214,172,148,.8), rgba(214,172,148,0) 100%),
      radial-gradient(ellipse 150px 190px at 52% 62%, rgba(110,82,62,.75), rgba(110,82,62,0) 100%),
      radial-gradient(ellipse 130px 200px at 66% 84%, rgba(236,232,228,.95), rgba(236,232,228,0) 100%),
      radial-gradient(ellipse 110px 180px at 92% 78%, rgba(40,36,36,.85), rgba(40,36,36,0) 100%),
      linear-gradient(90deg, rgba(255,255,255,0) 0%, rgba(214,200,188,.5) 28%, rgba(170,145,125,.8) 55%, rgba(120,100,88,.9) 100%);
    -webkit-mask-image: linear-gradient(180deg, transparent 0%, #000 30%, #000 100%);
            mask-image: linear-gradient(180deg, transparent 0%, #000 30%, #000 100%);
  }
  .hero-device {
    left: 840px; top: 120px; width: 276px; height: 454px; border-radius: 40px 40px 0 0;
    background: linear-gradient(160deg, #4a4a4a 0%, #111 30%, #000 100%); border: 3px solid #bbb; border-bottom: 0;
  }
  .hero-copy { left: 70px; top: 252px; width: 400px; }
  .hero-kicker { font: 500 34px/1.1 var(--heading); color: var(--green); }
  .hero-title { font: 600 44px/1.1 var(--heading); color: #111; margin-top: 2px; }
  .hero-text { margin-top: 14px; font: 400 16.5px/1.3 var(--body); color: var(--muted); width: 384px; }
  .cta {
    left: 70px; top: 426px; width: 248px; height: 48px; border-radius: 5px;
    background: linear-gradient(#4fc447, #218a25); box-shadow: 0 2px 3px rgba(0,0,0,.3);
    display: flex; align-items: center; padding-left: 18px; gap: 10px;
    font: 500 24px/1 var(--heading); color: #fff; text-decoration: none;
  }
  .slider-dots { left: 73px; top: 496px; display: flex; gap: 7px; }
  .slider-dots span { width: 18px; height: 18px; border-radius: 50%; background: #3a3a3a; border: 2px solid #ccc; }
  .slider-dots span.is-active { background: var(--green); }

  /* feature band */
  .feature-band {
    left: 58px; top: 574px; width: 790px; height: 158px; border-radius: 0 0 0 8px;
    background: linear-gradient(var(--band-top), var(--band-bottom)); box-shadow: 0 2px 4px rgba(0,0,0,.35);
  }
  .feature { top: 30px; width: 214px; color: #fff; }
  .feature h3 { font: 700 17px/1.1 var(--body); }
  .feature p { font: 400 14.5px/1.2 var(--body); }
  .feature-sep { top: 14px; width: 1px; height: 128px; background: rgba(0,0,0,.25); box-shadow: 1px 0 rgba(255,255,255,.15); }
  .specialise {
    left: 840px; top: 574px; width: 310px; height: 158px; border-radius: 0 0 8px 0;
    background: linear-gradient(#4cc44c, #228d22); border: 1px solid #1d7a1d; color: #fff;
  }
  .specialise h3 { position: absolute; left: 34px; top: 26px; font: 700 17px/1 var(--body); }
  .platforms { position: absolute; left: 34px; top: 66px; display: flex; gap: 22px; }
  .platforms span { width: 44px; height: 44px; border-radius: 50%; background: #fff; }

  /* news */
  .news-title { font: 600 21px/1 var(--heading); color: #111; display: flex; align-items: center; gap: 8px; }
  .news-title em { font-style: normal; color: var(--green); }
  .news-item { margin-top: 16px; font: 400 14.5px/1.2 var(--body); color: #111; }
  .news-meta { font: 400 13.5px/1.2 var(--body); color: var(--green-dark); }
  .blog { left: 64px; top: 752px; width: 500px; }
  .tweets { left: 607px; top: 752px; width: 565px; }
  .tweet-mark { width: 22px; height: 22px; border-radius: 50%; background: #111; }

  /* footer */
  .site-footer { left: 0; top: 948px; width: 1200px; height: 122px; background: var(--footer); color: var(--footer-text); }
  .foot-col { top: 24px; font: 400 14.5px/20.4px var(--body); list-style: none; }
  .foot-sep { top: 26px; width: 1px; height: 82px; background: #555; }
  .foot-nav { right: 53px; top: 24px; font: 400 14.5px/1.4 var(--body); text-align: right; }
  .social { right: 53px; top: 76px; display: flex; gap: 22px; font: 400 14.5px/1 var(--body); }
  .social a { color: #fff; text-decoration: underline; display: flex; align-items: center; gap: 8px; }
  .social i { width: 17px; height: 17px; background: #4a7ac9; display: inline-block; }
</style>
</head>
<body>
<div class="page">

  <div class="abs hero-photo" role="img" aria-label="Photo of two young women smiling and looking at a smartphone"></div>
  <div class="abs hero-device" role="img" aria-label="Smartphone handset showing the BrindleApps name on its screen"></div>

  <div class="abs brand">
    <div class="brand-mark"></div>
    <div class="brand-name">BrindleApps</div>
  </div>

  <nav class="abs main-nav">
    <a href="#" class="is-current">Home</a>
    <a href="#">About</a>
    <a href="#">Services</a>
    <a href="#">App Platforms</a>
    <a href="#">Contact Us</a>
    <a href="#">Blog</a>
  </nav>

  <div class="abs hero-copy">
    <h2 class="hero-kicker">Get Your Idea working</h2>
    <h1 class="hero-title">We deliver quality</h1>
    <p class="hero-text">Lorem ipsum dolor sit amet, consectetur adipiscing elit. Quisque aliquet, lorem sit amet adipiscing viverra, felis purus vestibulum tellus, in malesua.</p>
  </div>

  <a class="abs cta" href="#">what’s your idea
    <svg width="26" height="26" viewBox="0 0 26 26"><circle cx="13" cy="13" r="12" fill="#fff"/><path d="M10 7.5 L18.5 13 L10 18.5 Z" fill="#2a932a"/></svg>
  </a>

  <div class="abs slider-dots"><span></span><span class="is-active"></span><span></span></div>

  <section class="abs feature-band">
    <div class="abs feature" style="left:25px">
      <h3>Curabitur dapibus</h3>
      <p>Donec erat lorem, volu tpatidnon bibendum elementum, egestas blandit tortor. Sed nec nulla orci. Sed laoreet, ipsum ac sollicitudin venenatis,</p>
    </div>
    <div class="abs feature-sep" style="left:256px"></div>
    <div class="abs feature" style="left:286px">
      <h3>Quisque venenatis</h3>
      <p>Nulla in mauris tellus. Cura bitur et tellus ut odio euismod conva llis ac nec nisi. Donec sed erat justo, a fringilla nibh. Nunc gravi da erat dolor.</p>
    </div>
    <div class="abs feature-sep" style="left:516px"></div>
    <div class="abs feature" style="left:546px">
      <h3>What’s New</h3>
      <p>Lorem ipsum dolor sit amet, con sectetur adipiscing elit. Quisque venenatis convallis mi, in tincidunt est iaculis non. Aliquam egestas, null Donec erat lorem.</p>
    </div>
  </section>

  <section class="abs specialise">
    <h3>We specialise</h3>
    <div class="platforms"><span></span><span></span><span></span><span></span></div>
  </section>

  <section class="abs blog">
    <h2 class="news-title">
      <svg width="22" height="20" viewBox="0 0 22 20"><ellipse cx="9" cy="8" rx="8" ry="6.5" fill="#111"/><path d="M4 13 L3 18 L9 14 Z" fill="#111"/><ellipse cx="15" cy="12" rx="6" ry="5" fill="#111" stroke="#fff" stroke-width="1.5"/></svg>
      <span>From our <em>Blog</em></span>
    </h2>
    <div class="news-item">
      <p>Lorem ipsum dolor sit amet, consectetur adipiscing elit. Maurisviverra sed pharetra sed, imperdiet sollic itudin velit lorem iouis uilsk.</p>
      <p class="news-meta">October 28, 2010 | 6:14 PM, Posted by Colin Ferrante</p>
    </div>
    <div class="news-item" style="margin-top:22px">
      <p>Nulla mattis tellus vel nunc feugiat blandit. Phasellus laoreet, justo corper fringilla, libero nisi congue est, at interdum sem nequ.</p>
      <p class="news-meta">October 27, 2010 | 6:10 PM, Posted by Dana Holwell</p>
    </div>
  </section>

  <section class="abs tweets">
    <h2 class="news-title"><span class="tweet-mark"></span><span>Latest <em>Tweet</em></span></h2>
    <div class="news-item">
      <p class="news-meta">Tue, 29 Jun 2010 12:30</p>
      <p>Website looking tired? You can win a whole new one here http://lnk.example/8ZyGGE #business #webdesign #startup</p>
    </div>
    <div class="news-item" style="margin-top:22px">
      <p class="news-meta">Tue, 29 Jun 2010 09:08</p>
      <p>Gov to review all of its websites, following a report into the cost of procuring &amp; maintaining sites - http://lnk.example/c3hwwF</p>
    </div>
  </section>

  <footer class="abs site-footer">
    <ul class="abs foot-col" style="left:67px">
      <li>Torvix apps</li><li>Lumet apps</li><li>Plimnet Apps</li><li>Quorvel Apps</li>
    </ul>
    <div class="abs foot-sep" style="left:192px"></div>
    <ul class="abs foot-col" style="left:212px">
      <li>Wendolite Apps</li><li>Web applications</li><li>Vub Apps</li><li>Social Media Marketing</li>
    </ul>
    <div class="abs foot-sep" style="left:386px"></div>
    <ul class="abs foot-col" style="left:413px">
      <li>App Consultative Services</li><li>Persona Driven Development</li><li>App Design/User Experience Design</li><li>App Development / Maintenance</li>
    </ul>
    <div class="abs foot-nav">
      <p>Home &nbsp;|&nbsp; About &nbsp;|&nbsp; Services &nbsp;|&nbsp; App Platforms &nbsp;|&nbsp; Contact Us &nbsp;|&nbsp; Blog</p>
      <p>Copyright © 2011 Brindle Apps. All rights reserved.</p>
    </div>
    <div class="abs social">
      <a href="#"><i></i>Join our Plimnet Fanpage</a>
      <a href="#"><i style="background:#6fc3e8"></i>Follow us on Drosk</a>
    </div>
  </footer>

</div>
</body>
</html>
```